Banner Design for Physiotherapy Business

I need a banner designed for a physiotherapy business. The word ‘Physiotherapy’ should be prominent at the top. I’ve attached a document outlining what text and a suggestion of a picture I’d like included. The photo I have suggested in the document won’t upload to artvolley though as the dimensions are too large. I am open to other photos being used though. I would like to see designs that use the colour orange (as seen in the example) or green preferrably. The dimensions need to be 841mm x 2055mm and provided in PDF, JPG, and PNG format and 300dpi in CMYK colour mode.

```html
<!DOCTYPE html>
<html lang="en">
<head>
<meta charset="utf-8">
<title>Physiotherapy Roll-up Banner</title>
<link href="https://fonts.googleapis.com/css2?family=Bebas+Neue&family=Montserrat:wght@700;800&family=Source+Sans+3:wght@400;600&display=swap" rel="stylesheet">
<style>
  :root {
    --page-bg: #e4e5e2;
    --banner-bg: #ffffff;
    --ink: #111111;
    --accent-red: #e8501e;
    --accent-orange: #f39322;
    --photo-light: #eef0f1;
    --photo-mid: #c9ccd0;
    --photo-deep: #8d9aa8;
  }
  * { margin: 0; padding: 0; box-sizing: border-box; }
  html, body { width: 1200px; height: 1200px; overflow: hidden; background: var(--page-bg); }
  .banner {
    position: absolute; left: 366px; top: 28px;
    width: 468px; height: 1144px;
    background: var(--banner-bg);
    overflow: hidden;
    font-family: "Source Sans 3", sans-serif;
    color: var(--ink);
  }
  .banner-art { position: absolute; inset: 0; }
  .title-text { font-family: "Bebas Neue", sans-serif; fill: var(--accent-red); }
  .services-heading {
    position: absolute; left: 0; width: 100%; top: 548px;
    text-align: center; font-family: "Montserrat", sans-serif; font-weight: 800;
    line-height: 1.1;
  }
  .services-heading .line-dark { font-size: 31px; color: var(--ink); padding-left: 20px; }
  .services-heading .line-accent { font-size: 30px; color: var(--accent-red); }
  .heading-rule {
    position: absolute; top: 632px; left: 112px; width: 258px; height: 1px; background: var(--ink);
  }
  .heading-rule::after {
    content: ""; position: absolute; left: 112px; top: -3px; width: 34px; height: 7px; background: var(--accent-red);
  }
  .service-list {
    position: absolute; top: 652px; left: 62px; list-style: none;
    font-size: 15.5px; line-height: 21.5px;
  }
  .service-list::before {
    content: ""; position: absolute; left: 7px; top: 10px; bottom: 10px; width: 1px; background: var(--accent-red);
  }
  .service-item { position: relative; padding-left: 26px; }
  .service-num {
    position: absolute; left: 0; top: 4px; width: 15px; height: 15px; border-radius: 50%;
    background: var(--accent-red); color: #fff; font-size: 8px; line-height: 15px; text-align: center;
  }
  .member-mark {
    position: absolute; left: 28px; top: 1046px; display: flex; align-items: center; gap: 10px;
  }
  .member-dot { width: 44px; height: 44px; border-radius: 50%; background: #1f7fd1; }
  .member-name {
    font-size: 13px; line-height: 1.15; font-weight: 600; color: #1f5fb8; width: 110px;
  }
  .appointment {
    position: absolute; right: 0; top: 1010px; width: 210px; padding: 10px 12px 10px 14px;
    background: var(--accent-red); color: #fff; border-radius: 8px 0 0 8px;
  }
  .appointment-title { font-family: "Montserrat", sans-serif; font-weight: 700; font-size: 13.5px; }
  .appointment-details { font-size: 10.5px; line-height: 1.25; }
</style>
</head>
<body>
  <main class="banner">
    <svg class="banner-art" width="468" height="1144" viewBox="0 0 468 1144" aria-hidden="false">
      <defs>
        <linearGradient id="photoTone" x1="0" y1="0" x2="1" y2="1">
          <stop offset="0" stop-color="var(--photo-light)"/>
          <stop offset="0.55" stop-color="var(--photo-mid)"/>
          <stop offset="1" stop-color="var(--photo-deep)"/>
        </linearGradient>
      </defs>
      <text class="title-text" x="24" y="128" font-size="120" textLength="420" lengthAdjust="spacingAndGlyphs">PHYSIOTHERAPY</text>
      <polygon role="img" aria-label="Photo of a smiling physiotherapist guiding an older man through a dumbbell arm exercise in a bright clinic"
        points="0,150 468,150 468,400 253,549 0,435" fill="url(#photoTone)"/>
      <polygon class="corner-left" points="0,435 82,497 0,570" fill="var(--accent-orange)"/>
      <polygon class="corner-right" points="468,400 336,494 468,590" fill="var(--accent-red)"/>
    </svg>

    <h2 class="services-heading">
      <span class="line-dark">WHAT WE</span><br>
      <span class="line-accent">TREAT / SERVICES</span>
    </h2>
    <div class="heading-rule"></div>

    <ol class="service-list">
      <li class="service-item"><span class="service-num">1</span>Arthritis</li>
      <li class="service-item"><span class="service-num">2</span>Back Pain / Neck Pain</li>
      <li class="service-item"><span class="service-num">3</span>Sciatic Pain</li>
      <li class="service-item"><span class="service-num">4</span>Sports Injuries</li>
      <li class="service-item"><span class="service-num">5</span>Repetitive Strain Injuries</li>
      <li class="service-item"><span class="service-num">6</span>Post Surgical Management<br>(Hip and Knee Arthroscopes,<br>Joint Replacement Surgery)</li>
      <li class="service-item"><span class="service-num">7</span>Shoulder Pain and Dysfunction</li>
      <li class="service-item"><span class="service-num">8</span>Tennis Elbow</li>
      <li class="service-item"><span class="service-num">9</span>Postural Pain</li>
      <li class="service-item"><span class="service-num">10</span>Workplace Injuries</li>
      <li class="service-item"><span class="service-num">11</span>Motor Vehicle Accidents</li>
      <li class="service-item"><span class="service-num">12</span>Women’s Health Issues</li>
      <li class="service-item"><span class="service-num">13</span>Clinical Exercise</li>
      <li class="service-item"><span class="service-num">14</span>Pre-employment Functional Assessments</li>
    </ol>

    <div class="member-mark">
      <span class="member-dot"></span>
      <span class="member-name">Allied Physio Network Member</span>
    </div>

    <div class="appointment">
      <div class="appointment-title">MAKE AN APPOINTMENT</div>
      <div class="appointment-details">Maple Grove Health Clinic<br>18 Larkin St, Brookvale VIC 3199<br>(03) 9555 0142</div>
    </div>
  </main>
</body>
</html>
```